Design a modern, premium front panel for a stand-up pouch

Design a modern, premium front for a stand-up pouch for VELUTRA. Product is for Urine/vomit/runny stool incidents indoors; quick cleanups before smell sets; nighttime/elderly pet accidents; travel/car mishaps.

It must instantly show it’s for dogs & cats and include three small step icons with labels: Sprinkle → Wait 1–5 min → Sweep. Front copy to include: VELUTRA, descriptor “Mineral Instant Absorber – for Dogs & Cats”, one benefits line “Fragrance-Free • 100 % Mineral • Odor-Binding • Low-Dust

Goal: clear who/what/how in under 3 seconds
Deliverables: AI/PDF + a pouch mockup;

Target Market(s)

• Dog & cat households in apartments/homes; new pet parents, senior pets, multi-pet homes. • Cleanliness & odor-sensitive buyers (allergies/asthma, fragrance-free preference). • Surfaces at risk: carpets/rugs, sofas, mattresses, car interiors.

Industry/Entity Type

Pet e-commerce and retail

Font styles to use
Other font styles liked:
• like attached images

Requirements
Nice to have
• light background, eco friendly

```html
<!DOCTYPE html>
<html lang="en">
<head>
<meta charset="utf-8">
<title>VELUTRA – Mineral Instant Absorber pouch front</title>
<link rel="stylesheet" href="https://fonts.googleapis.com/css2?family=Ubuntu:wght@300;400;500&display=swap">
<style>
  :root {
    --backdrop: #1a9fd9;
    --pouch-white: #fbfcfd;
    --navy: #2a4f9e;
    --navy-band: #2f5aa8;
    --orange: #d9661e;
    --ink-on-band: #ffffff;
    --illustration-tone: #e7eef8;
  }
  * { margin: 0; padding: 0; box-sizing: border-box; }
  html, body { width: 1200px; height: 2533px; overflow: hidden; }
  body {
    background: var(--backdrop);
    font-family: "Ubuntu", sans-serif;
    position: relative;
  }
  .pouch-front {
    position: absolute;
    left: 120px;
    top: 446px;
    width: 960px;
    height: 1640px;
    background: var(--pouch-white);
    border-radius: 28px;
    overflow: hidden;
  }
  .zip-line {
    position: absolute;
    left: 0; right: 0;
    top: 170px;
    height: 3px;
    background: #e9eef5;
  }
  .wordmark {
    position: absolute;
    top: 330px;
    left: 0; right: 0;
    text-align: center;
    font-weight: 300;
    font-size: 150px;
    letter-spacing: 4px;
    color: var(--navy);
    line-height: 1;
  }
  .descriptor {
    position: absolute;
    top: 560px;
    left: 0; right: 0;
    text-align: center;
    font-weight: 500;
    font-size: 56px;
    line-height: 84px;
    color: var(--orange);
  }
  .pet-illustration {
    position: absolute;
    left: 120px;
    top: 820px;
    width: 360px;
    height: 560px;
    border-radius: 160px 160px 40px 40px;
    background: linear-gradient(180deg, var(--illustration-tone), #f3f6fb);
  }
  .steps {
    position: absolute;
    left: 500px;
    top: 820px;
    width: 420px;
    list-style: none;
    text-align: center;
  }
  .step { margin-bottom: 34px; }
  .step-icon { display: block; margin: 0 auto 10px; }
  .step-label {
    font-size: 50px;
    font-weight: 400;
    color: var(--orange);
    line-height: 1;
  }
  .benefit-band {
    position: absolute;
    left: 0; bottom: 0;
    width: 960px;
    height: 290px;
  }
  .benefits {
    position: absolute;
    left: 0; right: 0;
    bottom: 62px;
    text-align: center;
    color: var(--ink-on-band);
    font-size: 40px;
    font-weight: 400;
    line-height: 64px;
  }
</style>
</head>
<body>
  <main class="pouch-front">
    <div class="zip-line"></div>

    <h1 class="wordmark">VELUTRA</h1>

    <p class="descriptor">Mineral Instant Absorber<br>for Dogs &amp; Cats</p>

    <div class="pet-illustration" role="img" aria-label="Line illustration of a smiling dog hugging a cat"></div>

    <ol class="steps">
      <li class="step">
        <svg class="step-icon" width="110" height="90" viewBox="0 0 110 90" aria-hidden="true">
          <g fill="var(--navy)">
            <circle cx="40" cy="20" r="6"/><circle cx="60" cy="28" r="6"/>
            <circle cx="30" cy="45" r="6"/><circle cx="52" cy="52" r="6"/>
            <circle cx="72" cy="48" r="6"/><circle cx="42" cy="72" r="6"/>
            <circle cx="64" cy="74" r="6"/>
          </g>
        </svg>
        <span class="step-label">Sprinkle</span>
      </li>
      <li class="step">
        <svg class="step-icon" width="90" height="90" viewBox="0 0 90 90" aria-hidden="true">
          <circle cx="45" cy="45" r="36" fill="none" stroke="var(--navy)" stroke-width="5"/>
          <path d="M45 22 V46 L60 56" fill="none" stroke="var(--navy)" stroke-width="5" stroke-linecap="round"/>
        </svg>
        <span class="step-label">Wait 1-5 min</span>
      </li>
      <li class="step">
        <svg class="step-icon" width="110" height="100" viewBox="0 0 110 100" aria-hidden="true">
          <line x1="96" y1="6" x2="56" y2="58" stroke="var(--navy)" stroke-width="5" stroke-linecap="round"/>
          <path d="M50 52 L66 64 L54 90 L30 74 Z" fill="var(--navy)"/>
          <g stroke="var(--navy)" stroke-width="3" stroke-linecap="round">
            <line x1="10" y1="70" x2="22" y2="70"/>
            <line x1="6" y1="80" x2="22" y2="82"/>
          </g>
        </svg>
        <span class="step-label">Sweep</span>
      </li>
    </ol>

    <svg class="benefit-band" viewBox="0 0 960 290" preserveAspectRatio="none" aria-hidden="true">
      <path d="M0 20 C60 0 100 50 160 40 C220 30 250 0 320 10 C390 20 420 50 480 40 C540 30 580 0 640 10 C700 20 740 50 800 40 C860 30 900 0 960 10 L960 290 L0 290 Z" fill="var(--navy-band)"/>
    </svg>
    <p class="benefits">Fragrance-Free, 100 % Mineral<br>Odor-Binding, Low-Dust</p>
  </main>
</body>
</html>
```